PowerPoint Presentation Design < 10 Slides

Would like to update the following presentation to have a consistent theme and organization of the content. Following tolvenbrook.com or Quillmarsh4040.com.

Speaking at a conference would like to have a great public facing design!

Target Market(s)

Postal and parcel delivery industry

Colors
3176b5

Requirements
Must have
• Modern and consistent theme.
• Professional, Business focused.
Nice to have
• Engaging and thought provoking.

```html
<!DOCTYPE html>
<html lang="en">
<head>
<meta charset="utf-8">
<title>Tolvenbrook – First Mile Last Mile Slides</title>
<link rel="stylesheet" href="https://fonts.googleapis.com/css2?family=Montserrat:wght@300;400;600;700&family=Nunito+Sans:wght@400;600;700;800&display=swap">
<style>
  :root{
    --brand-blue:#3176b5;
    --bright-blue:#2f86d6;
    --navy:#0d1240;
    --deep-navy:#0a1a3c;
    --amber:#f5a623;
    --orange:#f2662b;
    --ink:#1d1d24;
    --white:#ffffff;
    --canvas:#ffffff;
  }
  *{box-sizing:border-box;margin:0;padding:0}
  html,body{width:1200px;height:1200px;overflow:hidden;background:var(--canvas)}
  body{position:relative;font-family:"Nunito Sans",Arial,sans-serif}

  .slide{position:absolute;overflow:hidden;color:var(--white)}
  .slide .photo{position:absolute;inset:0}

  .wordmark{position:absolute;font-family:"Montserrat",Arial,sans-serif;font-weight:300;
    letter-spacing:.12em;color:var(--white);line-height:1}

  /* title slide */
  .title-slide .photo{
    background:
      radial-gradient(ellipse 17% 13% at 55% 40%,#ffe36a 0%,#ffc21f 45%,rgba(245,166,35,0) 100%),
      radial-gradient(ellipse 32% 22% at 56% 44%,rgba(214,120,30,.85) 0%,rgba(150,80,30,.45) 45%,rgba(20,40,90,0) 100%),
      radial-gradient(ellipse 40% 30% at 85% 25%,rgba(40,70,140,.55) 0%,rgba(20,40,90,0) 100%),
      radial-gradient(ellipse 45% 35% at 20% 75%,rgba(35,60,125,.5) 0%,rgba(20,40,90,0) 100%),
      linear-gradient(160deg,#1a3572 0%,#102658 45%,#0a1842 75%,#060f2c 100%)}
  .title-slide .headline{position:absolute;left:6.5%;top:7.5%;font-family:"Montserrat",Arial,sans-serif;
    font-weight:700;font-size:1.75em;line-height:1.15;letter-spacing:.01em}
  .title-slide .headline .accent{color:var(--brand-blue)}
  .title-slide .tagline{position:absolute;left:6.5%;top:21%;font-family:"Montserrat",Arial,sans-serif;
    font-size:.74em;letter-spacing:.02em}
  .title-slide .contact{position:absolute;left:6.5%;bottom:9%;font-family:"Montserrat",Arial,sans-serif;
    font-size:.7em;line-height:1.2}
  .title-slide .contact small{display:block;font-size:.85em}
  .title-slide .guide{position:absolute;inset:0}
  .title-slide .wordmark{right:5%;bottom:8%;font-size:2.9em}

  .hero{left:363px;top:56px;width:485px;height:287px;font-size:10px}
  .tile{width:389px;height:292px;font-size:9.4px}
  .r1{top:500px}.r2{top:803px}
  .c1{left:12px}.c2{left:409px}.c3{left:805px}
  .tile .wordmark{font-size:2.25em;left:3.6%;bottom:5%}
  .title-slide.tile .wordmark{left:auto;right:5%;bottom:7%;font-size:2.9em}

  .kicker{font-weight:800;text-transform:uppercase;line-height:1.1}

  /* highway */
  .highway .photo{background:
      radial-gradient(ellipse 30% 22% at 18% 55%,#fffbe9 0%,rgba(255,240,190,0) 100%),
      radial-gradient(ellipse 55% 45% at 30% 50%,#ffe3a0 0%,rgba(247,190,90,.7) 50%,rgba(230,140,40,0) 100%),
      radial-gradient(ellipse 30% 30% at 45% 72%,rgba(110,45,15,.85) 0%,rgba(110,45,15,0) 100%),
      radial-gradient(ellipse 45% 80% at 92% 55%,rgba(70,30,12,.9) 0%,rgba(70,30,12,0) 100%),
      linear-gradient(120deg,#f6c36a 0%,#e39532 35%,#c0651f 60%,#7a3514 85%,#3e1a0b 100%)}
  .highway .copy{position:absolute;left:3.6%;top:9%;color:var(--ink)}
  .highway .small{font-size:1.75em}
  .highway .big{font-size:4.4em;color:var(--brand-blue);line-height:.95;margin:.02em 0 .08em}
  .highway .wordmark{color:#fbeedd}

  /* drone */
  .drone .photo{background:
      radial-gradient(ellipse 35% 10% at 45% 45%,rgba(255,236,170,.95) 0%,rgba(255,236,170,0) 100%),
      radial-gradient(ellipse 25% 14% at 65% 50%,rgba(40,42,50,.55) 0%,rgba(40,42,50,0) 100%),
      linear-gradient(180deg,#5d6068 0%,#7d7b78 18%,#b8a583 32%,#f0cf8a 43%,#cdb186 50%,#8f877f 60%,#5e5d63 72%,#3f3f46 84%,#2c2c31 100%)}
  .drone .copy{position:absolute;left:3.6%;top:7%;color:var(--ink)}
  .drone .big{font-size:4.4em;color:var(--brand-blue);line-height:1}
  .drone .small{font-size:1.5em}

  /* pickup */
  .pickup{background:var(--navy)}
  .pickup .photo{inset:auto;left:0;top:60px;width:252px;height:174px;background:
      radial-gradient(ellipse 25% 45% at 68% 55%,rgba(250,240,235,.75) 0%,rgba(250,240,235,0) 100%),
      linear-gradient(180deg,rgba(0,0,0,0) 55%,rgba(200,70,30,.5) 75%,#e7d3c8 100%),
      linear-gradient(100deg,#e24d1c 0%,#ea5f26 50%,#f07a3e 100%)}
  .pickup .panel{position:absolute;left:214px;top:91px;width:175px;height:110px;background:var(--navy);padding:15px 0 0 7px}
  .pickup .panel h3{font-weight:800;font-size:1.9em;line-height:1.15;color:var(--amber);text-transform:uppercase}
  .pickup .panel p{font-size:.98em;line-height:1.3;margin-top:5px}

  /* parachute */
  .parachute .photo{background:
      radial-gradient(ellipse 28% 24% at 68% 37%,rgba(240,245,252,.55) 0%,rgba(240,245,252,0) 100%),
      radial-gradient(ellipse 12% 10% at 87% 78%,rgba(230,80,60,.55) 0%,rgba(230,80,60,0) 100%),
      linear-gradient(180deg,#2f80d2 0%,#2a79c8 60%,#2a74c0 100%)}
  .parachute .copy{position:absolute;left:3.6%;top:125px}
  .parachute .big{font-size:3em;color:var(--amber)}
  .parachute .small{font-size:1.5em;margin-top:2px}

  /* technology */
  .tech .photo{background:radial-gradient(ellipse 70% 40% at 65% 100%,#2a82d6 0%,rgba(29,105,184,.5) 40%,transparent 75%),
      radial-gradient(ellipse 40% 30% at 10% 90%,rgba(29,105,184,.45) 0%,transparent 80%),
      linear-gradient(180deg,#0b1b3a 0%,#0a2350 100%)}
  .tech .heading{position:absolute;left:3.6%;top:22px;font-size:1.72em}
  .tech .columns{position:absolute;left:23px;top:83px;display:flex;gap:7px}
  .tech .col{width:63px;height:117px;background:var(--white);position:relative}
  .tech .col-head{background:var(--amber);height:41px;padding:5px 0 0 10px;color:var(--ink);
    font-weight:700;font-size:.8em;line-height:1.15;position:relative}
  .tech .col-head::after{content:"";position:absolute;right:10px;bottom:-5px;border:5px solid transparent;
    border-bottom:0;border-top-color:var(--brand-blue)}
  .tech .col-head.center{padding:13px 0 0 0;text-align:center}
  .tech .col ul{list-style:none;color:var(--ink);font-size:.55em;line-height:1.3;padding:10px 3px 0 5px}
  .tech .col li::before{content:"· "}
  .tech .timeline{position:absolute;left:23px;top:194px;width:343px;height:18px}
</style>
</head>
<body>

<section class="slide title-slide hero" aria-label="Title slide">
  <div class="photo" role="img" aria-label="Dark blue 3D cube field with one glowing amber cube"></div>
  <svg class="guide" viewBox="0 0 485 287" preserveAspectRatio="none" aria-hidden="true">
    <line x1="104" y1="75" x2="249" y2="222" stroke="#3176b5" stroke-width="1"/>
    <line x1="249" y1="222" x2="462" y2="222" stroke="#3176b5" stroke-width="1.2"/>
    <circle cx="249" cy="222" r="3" fill="#3176b5"/>
  </svg>
  <h1 class="headline">FIRST MILE <span class="accent">LAST MILE</span><br>OPPORTUNITIES</h1>
  <p class="tagline">Innovation &nbsp;I&nbsp; Inspiration &nbsp;I&nbsp; Obligations</p>
  <p class="contact">Tolvenbrook Group<small>Dana.Marlow@tolvenbrook.com</small></p>
  <span class="wordmark">tolvenbrook</span>
</section>

<section class="slide title-slide tile r1 c1" aria-label="Title slide">
  <div class="photo" role="img" aria-label="Dark blue 3D cube field with one glowing amber cube"></div>
  <svg class="guide" viewBox="0 0 389 292" preserveAspectRatio="none" aria-hidden="true">
    <line x1="84" y1="75" x2="200" y2="226" stroke="#3176b5" stroke-width="1"/>
    <line x1="200" y1="226" x2="370" y2="226" stroke="#3176b5" stroke-width="1.2"/>
    <circle cx="200" cy="226" r="2.6" fill="#3176b5"/>
  </svg>
  <h1 class="headline">FIRST MILE <span class="accent">LAST MILE</span><br>OPPORTUNITIES</h1>
  <p class="tagline">Innovation &nbsp;I&nbsp; Inspiration &nbsp;I&nbsp; Obligations</p>
  <p class="contact">Tolvenbrook Group<small>Dana.Marlow@tolvenbrook.com</small></p>
  <span class="wordmark">tolvenbrook</span>
</section>

<section class="slide tile highway r1 c2" aria-label="Red car slide">
  <div class="photo" role="img" aria-label="Photo from a speeding car: side mirror and dashboard with streaking amber light trails"></div>
  <div class="copy">
    <p class="kicker small">Have you<br>ever looked for a</p>
    <p class="kicker big">Red car</p>
    <p class="kicker small">On the highway?</p>
  </div>
  <span class="wordmark">tolvenbrook</span>
</section>

<section class="slide tile drone r1 c3" aria-label="Drone delivery slide">
  <div class="photo" role="img" aria-label="Photo of a quadcopter drone flying over mountains at sunset"></div>
  <div class="copy">
    <p class="kicker big">Drone</p>
    <p class="kicker small">Delivery of kidney<br>for transplant</p>
  </div>
  <span class="wordmark">tolvenbrook</span>
</section>

<section class="slide tile pickup r2 c1" aria-label="Buy online pickup at store slide">
  <div class="photo" role="img" aria-label="Photo of an orange in-store pickup area with a self-service kiosk and seating"></div>
  <div class="panel">
    <h3>Buy online<br>pickup at store</h3>
    <p>Just in time baby shower gift for 15<sup>th</sup><br>great grandchild</p>
  </div>
  <span class="wordmark">tolvenbrook</span>
</section>

<section class="slide tile parachute r2 c2" aria-label="Parachute medical supplies slide">
  <div class="photo" role="img" aria-label="Photo of a fixed-wing delivery drone releasing a parcel on a small parachute against a blue sky"></div>
  <div class="copy">
    <p class="kicker big">Parachute</p>
    <p class="kicker small">Vital medical supplies</p>
  </div>
  <span class="wordmark">tolvenbrook</span>
</section>

<section class="slide tile tech r2 c3" aria-label="Technology to enable innovation slide">
  <div class="photo" role="img" aria-label="Dark blue background with a glowing network of connected points"></div>
  <h2 class="kicker heading">Technology to enable innovation</h2>
  <div class="columns">
    <div class="col"><div class="col-head">Data - Real<br>Time</div>
      <ul><li>Streaming Analytics</li><li>Federated Data Sources</li></ul></div>
    <div class="col"><div class="col-head center">Algorithms</div>
      <ul><li>Machine learning</li><li>Predictive analytics</li><li>Optimization</li></ul></div>
    <div class="col"><div class="col-head center">Collaboration</div>
      <ul><li>Machine to Machine</li><li>Organization to Organization</li><li>Internet of Things</li><li>Smart Cities</li></ul></div>
    <div class="col"><div class="col-head">Autonomous<br>Operations</div>
      <ul><li>Self Driving vehicles</li><li>Self organizing machines</li></ul></div>
    <div class="col"><div class="col-head">User<br>Experience</div>
      <ul><li>Omni channel</li><li>Interactive</li><li>Convenient</li></ul></div>
  </div>
  <svg class="timeline" viewBox="0 0 343 18" aria-hidden="true">
    <line x1="31" y1="9" x2="324" y2="9" stroke="#3176b5" stroke-width="3"/>
    <line x1="31" y1="9" x2="324" y2="9" stroke="#f5a623" stroke-width="1.5" stroke-dasharray="20 50"/>
    <g fill="#f5a623" stroke="#0a2350" stroke-width="1">
      <circle cx="31" cy="9" r="7.5"/><circle cx="101" cy="9" r="7.5"/><circle cx="171" cy="9" r="7.5"/>
      <circle cx="241" cy="9" r="7.5"/><circle cx="311" cy="9" r="7.5"/>
    </g>
    <g fill="#1d1d24">
      <rect x="28" y="5" width="6" height="8" rx="1"/>
      <circle cx="101" cy="9" r="3.5" fill="none" stroke="#1d1d24" stroke-width="1.2"/>
      <circle cx="168" cy="7" r="2"/><circle cx="174" cy="7" r="2"/><rect x="166" y="10" width="10" height="3" rx="1"/>
      <rect x="236" y="8" width="10" height="4" rx="1.5"/>
      <circle cx="309" cy="8" r="2.2"/><rect x="306" y="11" width="6" height="3" rx="1"/>
    </g>
  </svg>
  <span class="wordmark">tolvenbrook</span>
</section>

</body>
</html>
```